Real Estate Business Cards

Looking for a clean, sharp and professional look for our Real Estate investment Fund that invests in Multi Family Apartment buildings.

Target Market(s)

Real Estate Fund

Industry/Entity Type

Real Estate

Contact Information for Business Card

Company Description: Real Estate Investment Fund
Company Name: RKW Holdings
Name: Marcus Olvane
Cell: (917) 482-0657
Email: marcus@rkwholdings-example.com
Website: www.rkwholdings-example.com
Address: 418, 9th Street, Brooklyn NY 11218

Colors

Designer to choose colors to be used in the design.

Requirements
Nice to have
• Colors to match logo

```html
<!DOCTYPE html>
<html lang="en">
<head>
<meta charset="utf-8">
<title>RKW Holdings – Business Card</title>
<link href="https://fonts.googleapis.com/css2?family=Roboto:wght@400;500&family=Cormorant+Garamond:wght@500&display=swap" rel="stylesheet">
<style>
  :root {
    --page-bg: #e9e4d8;
    --card-dark: #4a4a4a;
    --card-light: #ffffff;
    --brand-blue: #1470a8;
    --text-light: #ffffff;
  }
  * { margin: 0; padding: 0; box-sizing: border-box; }
  html, body {
    width: 1200px; height: 716px; overflow: hidden;
    background: var(--page-bg);
  }
  .canvas { position: relative; width: 1200px; height: 716px; }
  .card {
    position: absolute; left: 359px; width: 551px; height: 314px;
    border-radius: 12px; overflow: hidden; background: var(--card-dark);
  }
  .card--front { top: 31px; }
  .card--back { top: 367px; }
  .front-shape { position: absolute; inset: 0; }
  .front-brand {
    position: absolute; left: 20px; top: 146px; width: 240px;
    text-align: center;
    font-family: 'Roboto', sans-serif; font-weight: 500; font-size: 22px;
    color: var(--brand-blue); letter-spacing: 0.5px;
  }
  .contact {
    position: absolute; left: 326px; top: 81px;
    font-family: 'Roboto', sans-serif; color: var(--text-light);
    font-size: 13px; line-height: 15.5px;
  }
  .contact__name { font-size: 18px; font-weight: 500; line-height: 20px; letter-spacing: 0.3px; }
  .contact__role { margin-bottom: 10px; }
  .contact__company { font-weight: 500; font-size: 14px; }
  .contact__address { margin-bottom: 10px; }
  .contact__line { display: flex; align-items: center; gap: 4px; line-height: 17.5px; }
  .contact__icon { width: 11px; height: 11px; flex: none; }
  .back-brand {
    position: absolute; left: 0; right: 0; top: 138px;
    display: flex; justify-content: center; align-items: center; gap: 14px;
  }
  .back-brand__mark { width: 22px; height: 22px; background: var(--brand-blue); }
  .back-brand__name {
    font-family: 'Cormorant Garamond', serif; font-weight: 500;
    font-size: 36px; color: var(--text-light); letter-spacing: 1px;
  }
</style>
</head>
<body>
<div class="canvas">

  <section class="card card--front">
    <svg class="front-shape" viewBox="0 0 551 314" width="551" height="314">
      <path d="M0 0 H162 L305 150 Q313 158 305 166 L165 314 H0 Z" fill="var(--brand-blue)"/>
      <path d="M0 0 H155 L297 150 Q304 158 297 166 L158 314 H0 Z" fill="var(--card-light)"/>
      <path d="M0 0 H152 L294 150 Q301 158 294 166 L155 314 H0 Z" fill="var(--card-light)"/>
    </svg>
    <div class="front-brand">RKW Holdings</div>

    <div class="contact">
      <div class="contact__name">MARCUS OLVANE</div>
      <div class="contact__role">Owner</div>
      <div class="contact__company">RKW Holdings</div>
      <div>418, 9th Street</div>
      <div class="contact__address">Brooklyn NY 11218</div>
      <div class="contact__line">
        <svg class="contact__icon" viewBox="0 0 24 24"><path fill="#fff" d="M6.6 10.8a15 15 0 0 0 6.6 6.6l2.2-2.2c.3-.3.7-.4 1-.2 1.1.4 2.3.6 3.6.6.6 0 1 .4 1 1V20c0 .6-.4 1-1 1A17 17 0 0 1 3 4c0-.6.4-1 1-1h3.5c.6 0 1 .4 1 1 0 1.3.2 2.5.6 3.6.1.3 0 .7-.2 1z"/></svg>
        (917) 482-0657
      </div>
      <div class="contact__line">
        <svg class="contact__icon" viewBox="0 0 24 24"><path fill="#fff" d="M2 5h20v14H2z"/><path d="M2 5l10 8 10-8M2 19l7-7M22 19l-7-7" stroke="#4a4a4a" stroke-width="2" fill="none"/></svg>
        marcus@rkwholdings-example.com
      </div>
      <div class="contact__line">
        <svg class="contact__icon" viewBox="0 0 24 24" fill="none" stroke="#fff" stroke-width="2"><circle cx="12" cy="12" r="10"/><ellipse cx="12" cy="12" rx="4.5" ry="10"/><path d="M2 12h20M4 7h16M4 17h16"/></svg>
        www.rkwholdings-example.com
      </div>
    </div>
  </section>

  <section class="card card--back">
    <div class="back-brand">
      <span class="back-brand__mark"></span>
      <span class="back-brand__name">RKW Holdings</span>
    </div>
  </section>

</div>
</body>
</html>
```